Business Cards Needed

Hi designers, I have a new logo that was created by one of the ArtMingle designers. I'd now like to use that logo to make business cards. The company is called VitaLumen Advisors and is a business consulting firm. I'd like the business cards to be horizontal, modern, and professional.
I'd like the following information to be on the business card:
1) Logo
2) my name - Marisa Kolvane
3) my title - Principal
4) name of business - VitaLumen Advisors
5) mobile - 508.372.9146
6) e-mail - marisa@vitalumenadvisors.example
I'm uploading a JPG file of the logo. I'm hoping this is the correct file format. Please let me know if you need another type of file. Thank you.
Look and feel
Each slider illustrates characteristics of the customer's brand and the style your logo design should communicate.

```html
<!DOCTYPE html>
<html lang="en">
<head>
<meta charset="utf-8">
<title>VitaLumen Advisors – Business Card</title>
<link href="https://fonts.googleapis.com/css2?family=Roboto:wght@300;400;700&display=swap" rel="stylesheet">
<style>
  :root {
    --brand-blue: #1276bb;
    --brand-green: #7dbb3a;
    --card-white: #f5f5f4;
    --ink: #333333;
    --rule-blue: #2a6fae;
    --backdrop: #232323;
    --on-blue: #ffffff;
  }
  * { margin: 0; padding: 0; box-sizing: border-box; }
  html, body {
    width: 1200px; height: 1059px; overflow: hidden;
    background: var(--backdrop);
    font-family: "Roboto", Arial, sans-serif;
  }
  .stage { position: relative; width: 1200px; height: 1059px; }
  .card {
    position: absolute; left: 255px;
    width: 690px; height: 391px;
    border-radius: 18px; overflow: hidden;
  }
  .card--front { top: 89px; background: var(--card-white); }
  .card--back { top: 547px; background: var(--brand-blue); }

  .wordmark {
    position: absolute; font-weight: 400; white-space: nowrap;
  }
  .card--front .wordmark {
    right: 42px; top: 62px;
    font-size: 32px; color: var(--brand-blue);
  }
  .card--back .wordmark {
    left: 0; right: 0; top: 168px; text-align: center;
    font-size: 44px; color: var(--on-blue);
  }

  .accent-bar {
    position: absolute; left: 0; top: 222px;
    width: 19px; height: 44px; background: var(--brand-blue);
  }
  .person { position: absolute; left: 39px; top: 218px; }
  .person__name {
    font-size: 25px; font-weight: 700; letter-spacing: 0.2px; line-height: 1.1;
    text-transform: uppercase;
  }
  .person__first { color: var(--brand-blue); }
  .person__last { color: var(--brand-green); }
  .person__title { font-size: 16px; color: var(--ink); margin-top: 2px; }

  .divider {
    position: absolute; left: 39px; top: 279px;
    width: 610px; height: 1px; background: var(--rule-blue);
  }
  .contact {
    position: absolute; display: flex; align-items: center; gap: 7px;
    font-size: 16.5px; color: var(--ink); white-space: nowrap;
  }
  .contact svg { width: 13px; height: 13px; fill: var(--brand-green); flex: none; }
  .contact--phone { left: 39px; top: 297px; }
  .contact--email { left: 39px; top: 323px; }
  .contact--web { right: 42px; top: 323px; }
</style>
</head>
<body>
<main class="stage">
  <section class="card card--front" aria-label="Business card front">
    <div class="wordmark">VitaLumen Advisors</div>
    <div class="accent-bar"></div>
    <div class="person">
      <div class="person__name"><span class="person__first">Marisa</span> <span class="person__last">Kolvane</span></div>
      <div class="person__title">Principal</div>
    </div>
    <div class="divider"></div>
    <div class="contact contact--phone">
      <svg viewBox="0 0 16 16" aria-hidden="true"><path d="M1 6c0-2 3-3 7-3s7 1 7 3v1.5h-3.5V6c-1-.5-6-.5-7 0v1.5H1z"/><path d="M3.5 9l2-2h5l2 2v5h-9z"/></svg>
      <span>508.372.9146</span>
    </div>
    <div class="contact contact--email">
      <svg viewBox="0 0 16 16" aria-hidden="true"><path d="M1 6l7-5 7 5v9H1z"/><path d="M2.5 7l5.5 4 5.5-4" fill="none" stroke="#f5f5f4" stroke-width="1.2"/></svg>
      <span>marisa@vitalumenadvisors.example</span>
    </div>
    <div class="contact contact--web">
      <svg viewBox="0 0 16 16" aria-hidden="true"><circle cx="8" cy="8" r="7"/><path d="M5 4c2 1 1 3 3 3s1 3 3 3" fill="none" stroke="#f5f5f4" stroke-width="1.3"/></svg>
      <span>www.vitalumenadvisors.example</span>
    </div>
  </section>

  <section class="card card--back" aria-label="Business card back">
    <div class="wordmark">VitaLumen Advisors</div>
  </section>
</main>
</body>
</html>
```